依頼詳細
作成はレスポンシブウェブデザインにて作成をしようと考えているのですが、
SEOにも配慮したデザインを希望してます。

WEBサイトの雰囲気としては
http://lumivane.com/
上記のようなテイストを希望しています。
また、医療機関であり、患者さんがすぐに欲しい情報にたどり着けるよう
http://www.kozuetani-hp.or.jp/
上記のURLのような配置であれば診療時間やアクセスなどにすぐたどり着けて患者さんにとって利便性が高いと考えています。

・基本的に現行のサイトのページは全てリニューアルサイトに盛り込む予定
・基礎的なSEOを考慮して文字に関しては極力テキストで入れることを想定
・レスポンシブウェブデザインを前提としたデザイン

した上で、デザインをお願いできれば幸いです。
サイトURL
http://www.sorvane-dc.jp/
ページ数
2ページ
希望イメージ
シンプル 複雑
単色 カラフル
暗い 明るい
日常 高級
遊び心 厳粛
未来的 伝統的
女性的 男性的
希望する色
白をベースに清潔感かつモダンなイメージ
納品ファイル
• 高解像度JPG (.jpg)
• イラストレーター形式 (.ai)
補足説明

SEOを考えたときにある程度文字を入れるスペースを欲しかったので、そのような部分も確保しつつサイトのデザインが私のイメージに最も近かったので選ばせて頂きました。

皆様からの多数のご応募ありがとうございました。また次の機会もありましたらよろしくお願い致します。

```html
<!DOCTYPE html>
<html lang="ja">
<head>
<meta charset="utf-8">
<title>ソルヴェイン歯科クリニック</title>
<link rel="stylesheet" href="https://fonts.googleapis.com/css2?family=Noto+Sans+JP:wght@400;700&display=swap">
<style>
:root{
  --teal:#22b3a2;
  --teal-dark:#178f82;
  --teal-light:#e3f5f2;
  --ink:#444;
  --muted:#888;
  --line:#d9d9d9;
  --bg:#f3f3f3;
  --white:#fff;
  --red:#d9534f;
}
*{box-sizing:border-box;margin:0;padding:0}
html,body{width:773px;height:1200px;overflow:hidden}
body{background:var(--bg);font-family:"Noto Sans JP",sans-serif;color:var(--ink);font-size:8px;line-height:1.5}
.page{position:relative;width:773px;height:1200px}
.sidebar{position:absolute;left:72px;top:13px;width:208px}
.main{position:absolute;left:288px;top:13px;width:414px}

.logo{height:78px;background:var(--white);display:flex;flex-direction:column;align-items:center;justify-content:center;gap:2px}
.logo .jp{font-size:13px;font-weight:700;color:var(--teal-dark);display:flex;align-items:center;gap:6px}
.logo .jp i{width:10px;height:10px;border-radius:50%;background:var(--teal);display:inline-block}
.logo .en{font-size:9px;color:var(--teal-dark)}

.nav{margin-top:7px;list-style:none}
.nav li{height:23px;margin-bottom:1px;background:var(--teal);color:var(--white);font-size:8.5px;display:flex;align-items:center;padding-left:10px;position:relative}
.nav li::after{content:"";position:absolute;right:9px;width:5px;height:5px;border-top:1.5px solid #fff;border-right:1.5px solid #fff;transform:rotate(45deg)}
.nav li.current{background:var(--teal-dark);font-weight:700}

.call{margin-top:14px;background:var(--white);border:2px solid var(--teal);padding:8px 10px;height:166px}
.call .tel{font-size:15px;font-weight:700;color:var(--teal-dark);display:flex;align-items:center;gap:5px}
.call dl{margin-top:6px;font-size:7px;color:var(--muted);line-height:1.7}
.call .btn{margin-top:8px;background:var(--teal);color:#fff;text-align:center;padding:5px 0;font-size:8px}

.side-access{margin-top:22px}
.heading{font-size:12px;font-weight:700;color:var(--ink);border-bottom:2px solid var(--teal);padding-bottom:3px;margin-bottom:7px}
.map{height:163px;background:linear-gradient(135deg,#e8eee4,#d6e2d8);border:1px solid var(--line)}
.addr{font-size:7px;color:var(--muted);margin-top:4px}

.top{display:flex;gap:5px;height:206px}
.hero{width:240px;background:linear-gradient(180deg,#cfe3ee 0%,#e9eef0 45%,#bfc4c6 100%);position:relative}
.hero .tag{position:absolute;left:50%;top:8px;transform:translateX(-50%);background:var(--teal);color:#fff;font-size:8px;padding:2px 10px;white-space:nowrap}
.hours{flex:1;background:var(--white);display:flex;flex-direction:column}
.hours h2{background:var(--teal);color:#fff;font-size:9px;padding:5px 8px}
.hours table{width:100%;border-collapse:collapse;font-size:7.5px;margin-top:4px}
.hours td{padding:4px 6px;border-bottom:1px solid var(--line);vertical-align:top}
.hours .red{color:var(--red)}
.hours .closed{padding:5px 6px;font-size:7.5px}

.box{background:var(--white);margin-top:13px;padding:10px 12px}
.greeting{height:212px}
.greeting p{font-size:7px;color:#666;line-height:1.9}

.features{display:flex;gap:6px;margin-top:10px}
.feature{flex:1;height:110px;position:relative}
.feature .cap{position:absolute;left:0;bottom:0;background:#fff;font-size:8px;padding:2px 7px}
.f1{background:linear-gradient(135deg,#e5ddd0,#c9bba6)}
.f2{background:linear-gradient(135deg,#d7e2e6,#b6c6cc)}
.f3{background:linear-gradient(135deg,#f1d9d3,#e2b8ad)}

.menu{height:304px}
.menu-grid{display:grid;grid-template-columns:repeat(3,1fr);gap:10px 8px}
.item{display:flex;align-items:center;gap:6px}
.item .ph{width:62px;height:62px;flex:none}
.item span{font-size:8px}
.p1{background:linear-gradient(135deg,#f6dede,#e5a9a9)}
.p2{background:linear-gradient(135deg,#e2e6ea,#b8c2cb)}
.p3{background:linear-gradient(135deg,#f5e3dc,#dba89a)}
.p4{background:linear-gradient(135deg,#fff1d2,#a6d3cd)}
.p5{background:linear-gradient(135deg,#eddcd3,#c9a897)}
.p6{background:linear-gradient(135deg,#f0e2da,#caa28e)}
.p7{background:linear-gradient(135deg,#e4eef2,#aecbd6)}

.news{height:150px}
.news ul{list-style:none}
.news li{display:flex;gap:8px;align-items:center;font-size:7px;padding:4px 0;border-bottom:1px dotted var(--line)}
.news .label{background:var(--teal);color:#fff;padding:0 5px;font-size:6.5px}

.footer{position:absolute;left:0;right:0;top:1058px;text-align:center}
.footer .links{font-size:7.5px;color:var(--teal-dark)}
.footer .links span{margin:0 8px}
.footer .copy{font-size:7px;color:var(--muted);margin-top:6px}
</style>
</head>
<body>
<div class="page">
  <aside class="sidebar">
    <div class="logo">
      <div class="jp"><i></i>ソルヴェイン歯科クリニック</div>
      <div class="en">Sorvane dental clinic</div>
    </div>
    <ul class="nav">
      <li class="current">HOME</li><li>初めての方</li><li>医院案内</li><li>診療時間案内</li><li>スタッフ紹介</li><li>ドクター紹介</li><li>ホワイトニング</li><li>セレクト</li><li>インプラント</li><li>審美歯科</li><li>予防歯科</li><li>小児歯科</li><li>アンチエイジング</li><li>治療費用料金表</li><li>無料歯科検診</li><li>矯正歯科</li><li>訪問歯科</li><li>「かむ」教室</li><li>スタッフ募集</li><li>サイトマップ</li><li>アクセス</li><li>ブログ</li>
    </ul>
    <div class="call">
      <div class="tel">
        <svg width="14" height="14" viewBox="0 0 24 24"><path fill="#178f82" d="M6.6 10.8a15 15 0 0 0 6.6 6.6l2.2-2.2c.3-.3.7-.4 1-.2 1.1.4 2.3.6 3.6.6.6 0 1 .4 1 1V20c0 .6-.4 1-1 1A17 17 0 0 1 3 4c0-.6.4-1 1-1h3.5c.6 0 1 .4 1 1 0 1.3.2 2.5.6 3.6.1.3 0 .7-.2 1z"/></svg>
        0952-40-3186
      </div>
      <dl>
        <dt>平日　AM9:00〜PM6:00</dt>
        <dt>土曜日　AM9:00〜PM1:00</dt>
        <dt>休診日　日曜・祝日</dt>
        <dt>お気軽にお電話ください</dt>
      </dl>
      <div class="btn">メールでのお問い合わせ</div>
    </div>
    <section class="side-access">
      <h2 class="heading">アクセス</h2>
      <div class="map" role="img" aria-label="医院周辺の地図"></div>
      <p class="addr">〒840-0000 佐賀県佐賀市本町1-2-3<br>駐車場完備・駅から徒歩5分</p>
    </section>
  </aside>

  <main class="main">
    <div class="top">
      <div class="hero" role="img" aria-label="白い外壁の医院外観写真"><span class="tag">Sorvane dental clinic</span></div>
      <div class="hours">
        <h2>診療時間</h2>
        <table>
          <tr><td>平日</td><td>AM9:00〜PM1:00<br><span class="red">休憩時間 PM2:00</span></td></tr>
          <tr><td>土曜</td><td>AM9:00〜PM1:00<br><span class="red">休憩時間 PM2:00</span></td></tr>
        </table>
        <div class="closed">休診日　日曜・祝日</div>
      </div>
    </div>

    <section class="box greeting">
      <h2 class="heading">ご挨拶</h2>
      <p>佐賀市内に2014年に新しく歯科医院を開院いたしました。ホワイトニング、審美歯科、予防歯科、小児歯科、インプラントなど幅広い診療に対応しております。患者様お一人お一人のお悩みに丁寧に向き合い、痛みの少ない治療を心がけています。<br>当院ではお口の健康を通じて全身の健康を守ることを大切にしております。定期検診やクリーニングもお気軽にご相談ください。<br>明るく清潔な院内で、スタッフ一同笑顔でお待ちしております。ご不明な点がございましたらお気軽にお問い合わせください。</p>
    </section>

    <div class="features">
      <div class="feature f1" role="img" aria-label="院内の写真"><span class="cap">医院紹介</span></div>
      <div class="feature f2" role="img" aria-label="診療室の写真"><span class="cap">診療時間案内</span></div>
      <div class="feature f3" role="img" aria-label="白い歯の写真"><span class="cap">無料歯科検診</span></div>
    </div>

    <section class="box menu">
      <h2 class="heading">診療メニュー</h2>
      <div class="menu-grid">
        <div class="item"><div class="ph p1" role="img" aria-label="ホワイトニングの写真"></div><span>ホワイトニング</span></div>
        <div class="item"><div class="ph p2" role="img" aria-label="インプラントの写真"></div><span>インプラント</span></div>
        <div class="item"><div class="ph p3" role="img" aria-label="審美歯科の写真"></div><span>審美歯科</span></div>
        <div class="item"><div class="ph p4" role="img" aria-label="歯ブラシの写真"></div><span>予防歯科</span></div>
        <div class="item"><div class="ph p5" role="img" aria-label="小児歯科の写真"></div><span>小児歯科</span></div>
        <div class="item"><div class="ph p6" role="img" aria-label="歯周病治療の写真"></div><span>歯周病</span></div>
        <div class="item"><div class="ph p7" role="img" aria-label="透明な矯正装置の写真"></div><span>クリアアライナー</span></div>
      </div>
    </section>

    <section class="box news">
      <h2 class="heading">お知らせ</h2>
      <ul>
        <li>2015.02.16<span class="label">お知らせ</span>ホームページを公開いたしました。</li>
        <li>2015.02.06<span class="label">お知らせ</span>院内設備のご案内を更新しました。</li>
        <li>2015.01.28<span class="label">お知らせ</span>春季休診日のお知らせです。</li>
        <li>2015.01.20<span class="label">お知らせ</span>無料歯科検診の受付を開始しました。</li>
        <li>2015.01.15<span class="label">お知らせ</span>スタッフ紹介ページを追加しました。</li>
        <li>2015.01.02<span class="label">お知らせ</span>年始の診療についてのご案内です。</li>
      </ul>
    </section>
  </main>

  <footer class="footer">
    <div class="links"><span>サイトマップ</span><span>個人情報保護方針</span></div>
    <p class="copy">Copyright (C) 2014 Sorvane dental clinic. All Rights Reserved</p>
  </footer>
</div>
</body>
</html>
```